Signage Design Project

We need a logo and signage for the shopfront of a personal fitness training gym and coaching facility. We want the signage to cover the glass shopfront windows which consist of 4 glass windows with dimensions: 1 of 200cm x 180cm, 2 of 180cm x 135cm and 1 of 180cm x 180cm. The windows that are 200x 180 and 180x180 are the most visable/ important. We want the 200x180 to display the logo and our name which is "Harbourline Fitness Centre" with further information of: Your personal training studio and boutique coaching gym Ph: 9472 3815.
For the window with 180 x 180cm measurement we want to list the services we provide which are:
Personal Training Sessions | Group Classes|Weight Loss |Toning & Sculpting|Bodybuilding I Cardio|Weights| Kettlebells| Boxing| Circuits I Team Building Programs| Boot Camp I Healthy Lifestyle & Wellness Coaching
The 2 windows 180x135cm are diagonal to the entry of the shop. We want them to be the same and plainer in design with the words: Harbourline Fitness Centre
Personal Training Studio and Boutique Coaching Gym
The signage design also includes an acrylic window box that lights up which is to display the logo and Harbourline Fitness Centre

```html
<!DOCTYPE html>
<html lang="en">
<head>
<meta charset="utf-8">
<title>Harbourline Fitness Centre – Window Signage</title>
<link rel="stylesheet" href="https://fonts.googleapis.com/css2?family=Russo+One&family=Questrial&display=swap">
<style>
  :root {
    --page: #ffffff;
    --cap: #f2f2f2;
    --blue-light: #00b6ec;
    --blue-deep: #0a93c2;
    --orange-light: #f8a838;
    --orange-deep: #f27f2f;
    --ink: #f4f4f4;
  }
  html, body {
    margin: 0;
    padding: 0;
    overflow: hidden;
    background: var(--page);
  }
  .canvas {
    position: relative;
    width: 1200px;
    height: 900px;
    overflow: hidden;
    background: var(--page);
  }
  .sign {
    position: absolute;
    background: var(--cap);
    overflow: hidden;
  }
  .sign--blue { left: 32px; top: 214px; width: 565px; height: 509px; }
  .sign--orange { left: 609px; top: 212px; width: 566px; height: 510px; }
  .sign__wave {
    position: absolute;
    inset: 0;
    width: 100%;
    height: 100%;
  }
  .brand-mark {
    position: absolute;
    display: flex;
    align-items: center;
    gap: 10px;
    font-family: "Russo One", sans-serif;
    font-size: 17px;
    letter-spacing: 1px;
  }
  .brand-mark__dot {
    width: 58px;
    height: 58px;
    border-radius: 50%;
  }
  .sign--blue .brand-mark { left: 88px; top: 20px; color: var(--blue-deep); }
  .sign--blue .brand-mark__dot { background: var(--blue-deep); }
  .sign--orange .brand-mark { left: 48px; top: 36px; color: var(--orange-deep); }
  .sign--orange .brand-mark__dot { background: var(--orange-deep); }

  .title {
    position: absolute;
    margin: 0;
    font-family: "Russo One", sans-serif;
    font-weight: 400;
    color: var(--ink);
    line-height: 1;
    white-space: nowrap;
  }
  .sign--blue .title { left: 0; width: 565px; top: 142px; text-align: center; font-size: 58px; letter-spacing: 1px; }
  .sign--orange .title { left: 38px; top: 148px; font-size: 56px; letter-spacing: 1px; }

  .subtitle {
    position: absolute;
    color: var(--ink);
    white-space: nowrap;
    line-height: 1;
  }
  .sign--blue .subtitle {
    left: 90px; top: 228px; width: 369px; height: 66px;
    border: 4px solid var(--ink);
    border-radius: 16px;
    display: flex; align-items: center; justify-content: center;
    font-family: "Questrial", sans-serif;
    font-size: 36px;
  }
  .sign--orange .subtitle {
    left: 126px; top: 232px;
    font-family: "Russo One", sans-serif;
    font-size: 31px;
    letter-spacing: 2px;
  }

  .tagline {
    position: absolute;
    margin: 0;
    font-family: "Questrial", sans-serif;
    color: var(--ink);
    text-align: center;
    letter-spacing: 2.5px;
    line-height: 1.12;
  }
  .sign--blue .tagline { left: 0; width: 565px; top: 325px; font-size: 26px; }
  .sign--orange .tagline { left: 0; width: 552px; top: 308px; font-size: 25px; }

  .phone {
    position: absolute;
    margin: 0;
    font-family: "Questrial", sans-serif;
    color: var(--ink);
    letter-spacing: 4px;
    white-space: nowrap;
    line-height: 1;
  }
  .sign--blue .phone { left: 88px; top: 440px; font-size: 44px; }
  .sign--orange .phone { left: 100px; top: 430px; font-size: 42px; }
</style>
</head>
<body>
<div class="canvas">

  <section class="sign sign--blue">
    <svg class="sign__wave" viewBox="0 0 565 509" preserveAspectRatio="none" aria-hidden="true">
      <defs>
        <linearGradient id="blueFill" x1="0" y1="1" x2="1" y2="0">
          <stop offset="0" stop-color="var(--blue-deep)"/>
          <stop offset="0.7" stop-color="var(--blue-light)"/>
          <stop offset="1" stop-color="var(--blue-deep)"/>
        </linearGradient>
      </defs>
      <path d="M0,76 C140,125 300,100 420,48 C480,24 535,16 565,24 L565,509 L0,509 Z" fill="url(#blueFill)"/>
    </svg>
    <div class="brand-mark"><span class="brand-mark__dot"></span>Harbourline</div>
    <h1 class="title">HARBOURLINE</h1>
    <div class="subtitle">Fitness Centre</div>
    <p class="tagline">Your personal training<br>studio &amp; boutique<br>coaching gym</p>
    <p class="phone">Ph: 9472 3815</p>
  </section>

  <section class="sign sign--orange">
    <svg class="sign__wave" viewBox="0 0 566 510" preserveAspectRatio="none" aria-hidden="true">
      <defs>
        <radialGradient id="orangeFill" cx="0.4" cy="0.15" r="0.9">
          <stop offset="0" stop-color="var(--orange-light)"/>
          <stop offset="1" stop-color="var(--orange-deep)"/>
        </radialGradient>
      </defs>
      <path d="M0,80 C30,130 110,125 250,85 C380,48 480,20 530,60 C550,80 560,110 566,140 L566,510 L0,510 Z" fill="url(#orangeFill)"/>
    </svg>
    <div class="brand-mark"><span class="brand-mark__dot"></span>Harbourline</div>
    <h1 class="title">HARBOURLINE</h1>
    <div class="subtitle">Fitness Centre</div>
    <p class="tagline">Your personal training<br>studio &amp; boutique<br>coaching gym</p>
    <p class="phone">Ph: 9472 3815</p>
  </section>

</div>
</body>
</html>
```